Summit Brightway Realty Group & Greenleaf Lending Services, Inc.
Present Our
Annual Holiday Celebration

for Agents, Originators, Clients & Friends
All are Welcome!!

Catered by Chef Ramo Ramo
w/ DJ and Full Dance Floor

** No Cover Charge
Saturday, January 22, 2022
7 pm - 11 pm

at Velvet Parlor
4871 Q Street NE Washington DC 20019

Call Marcus Pelletier at (240) 555-0184 with questions.

```html
<!DOCTYPE html>
<html lang="en">
<head>
<meta charset="utf-8">
<title>Annual Holiday Celebration</title>
<link rel="stylesheet" href="https://fonts.googleapis.com/css2?family=Anton&family=Arimo:wght@400;700&family=Kaushan+Script&display=swap">
<style>
  :root {
    --teal: #00909f;
    --teal-band: #03939f;
    --blue-dark: #0a5fae;
    --blue-light: #1a7fd6;
    --red: #c8250c;
    --burst: #f0380d;
    --navy: #002c50;
    --ink: #111111;
    --white: #ffffff;
    --frame: #777777;
  }
  * { box-sizing: border-box; margin: 0; padding: 0; }
  html, body { width: 1200px; height: 1200px; overflow: hidden; background: var(--white); }
  .flyer { position: relative; width: 1200px; height: 1200px; background: var(--white); font-family: "Arimo", Arial, sans-serif; color: var(--ink); }
  .abs { position: absolute; }

  .bunting { left: 0; top: 0; width: 1200px; height: 180px;
    background: linear-gradient(90deg, rgba(240,90,20,.28), rgba(250,200,20,.28), rgba(60,170,40,.28), rgba(240,60,20,.28), rgba(250,200,20,.28), rgba(60,170,40,.28), rgba(240,80,20,.28));
    clip-path: polygon(0 50%, 100% 20%, 100% 95%, 0 100%); }
  .confetti { background: radial-gradient(circle, rgba(230,60,160,.18), rgba(255,255,255,0) 70%); }
  .confetti.left-top { left: 30px; top: 250px; width: 140px; height: 170px; background: radial-gradient(circle, rgba(230,180,30,.2), rgba(255,255,255,0) 70%); }
  .confetti.right-top { left: 1030px; top: 190px; width: 110px; height: 130px; background: radial-gradient(circle, rgba(40,160,60,.18), rgba(255,255,255,0) 70%); }
  .confetti.right-mid { left: 1040px; top: 350px; width: 120px; height: 180px; }
  .confetti.left-mid { left: 60px; top: 630px; width: 120px; height: 170px; }

  .portrait { left: 888px; top: 576px; width: 312px; height: 547px;
    background: linear-gradient(180deg, #cfc9c1 0%, #ddd8d1 40%, #c9c4bc 100%);
    clip-path: polygon(130px 0, 250px 0, 270px 100px, 312px 190px, 312px 547px, 0 547px, 20px 420px, 80px 260px, 120px 190px, 110px 100px); }

  .brand { font-family: "Arimo", Arial, sans-serif; font-weight: 700; color: var(--navy); font-size: 21px; line-height: 1.2; text-align: center; display: flex; align-items: center; justify-content: center; }
  .brand.realty { left: 336px; top: 140px; width: 254px; height: 100px; }
  .brand.lending { left: 616px; top: 140px; width: 250px; height: 100px; }

  .title-frame { left: 234px; top: 305px; width: 716px; height: 196px; border: 1px solid var(--frame); }
  .present { left: 476px; top: 276px; width: 232px; text-align: center; background: var(--white); font-size: 40px; line-height: 46px; }
  .headline { font-family: "Anton", Impact, sans-serif; color: var(--teal); text-align: center; line-height: 1; }
  .headline.line-one { left: 230px; top: 326px; width: 724px; font-size: 100px; letter-spacing: 1px; }
  .headline.line-two { left: 292px; top: 442px; width: 600px; font-size: 100px; letter-spacing: 1px; background: var(--white); }

  .ribbon { left: 244px; top: 576px; width: 716px; height: 124px; }
  .ribbon-text { left: 300px; top: 588px; width: 604px; text-align: center; color: var(--white); font-weight: 700; font-size: 44px; line-height: 50px; }

  .welcome { left: 250px; top: 712px; width: 700px; text-align: center; font-family: "Kaushan Script", cursive; color: var(--teal); font-size: 82px; line-height: 100px; }

  .date-box { left: 253px; top: 836px; width: 684px; height: 92px; border: 1.5px solid var(--ink); display: flex; align-items: center; justify-content: center; }
  .date { font-family: "Anton", Impact, sans-serif; color: var(--red); font-size: 53px; line-height: 1; white-space: nowrap; }

  .catering { left: 360px; top: 943px; width: 480px; text-align: center; font-weight: 700; font-size: 31px; line-height: 40px; }

  .burst { left: 0; top: 900px; width: 266px; height: 223px; overflow: hidden; }
  .burst-text { left: 8px; top: 980px; width: 232px; text-align: center; color: var(--white); }
  .burst-text .cover { font-weight: 700; font-size: 27px; line-height: 34px; }
  .burst-text .hours { font-family: "Anton", Impact, sans-serif; font-size: 36px; line-height: 50px; }

  .venue { left: 341px; top: 1039px; width: 527px; height: 84px; background: var(--navy); clip-path: polygon(18px 0, calc(100% - 18px) 0, 100% 22px, 100% 100%, 0 100%, 0 22px); color: var(--white); text-align: center; font-size: 22px; line-height: 34px; padding-top: 8px; }

  .contact-band { left: 0; top: 1123px; width: 1200px; height: 77px; background: var(--teal-band); color: var(--white); font-weight: 700; font-size: 32px; display: flex; align-items: center; justify-content: center; }
</style>
</head>
<body>
<main class="flyer">
  <div class="abs bunting" role="img" aria-label="Festive bunting of red, yellow and green pennant flags with confetti"></div>
  <div class="abs confetti left-top" role="img" aria-label="Gold curled streamer with confetti"></div>
  <div class="abs confetti right-top" role="img" aria-label="Green curled streamer"></div>
  <div class="abs confetti right-mid" role="img" aria-label="Pink curled streamer with confetti"></div>
  <div class="abs confetti left-mid" role="img" aria-label="Pink curled streamer with confetti"></div>

  <div class="abs portrait" role="img" aria-label="Photo of the caterer in a white chef's jacket, resting chin on hand"></div>

  <div class="abs brand realty">Summit Brightway<br>Realty Group</div>
  <div class="abs brand lending">Greenleaf Lending<br>Services, Inc.</div>

  <div class="abs title-frame"></div>
  <div class="abs present">Present Our</div>
  <h1 class="abs headline line-one">ANNUAL HOLIDAY</h1>
  <div class="abs headline line-two">CELEBRATION</div>

  <svg class="abs ribbon" viewBox="0 0 716 124" aria-hidden="true">
    <defs>
      <linearGradient id="ribbonFill" x1="0" x2="1" y1="0" y2="0">
        <stop offset="0" stop-color="#0a5fae"/>
        <stop offset="0.5" stop-color="#1a80d8"/>
        <stop offset="1" stop-color="#0a5fae"/>
      </linearGradient>
    </defs>
    <polygon points="0,0 716,0 643,62 716,124 0,124 73,62" fill="url(#ribbonFill)"/>
  </svg>
  <div class="abs ribbon-text">For Agents, Originators,<br>Clients &amp; Friends</div>

  <div class="abs welcome">All are Welcome!!</div>

  <div class="abs date-box"><span class="date">SATURDAY, JANUARY 22, 2022</span></div>

  <p class="abs catering">Catered by Chef Ramo Ramo w/ DJ and Full Dance Floor</p>

  <svg class="abs burst" viewBox="0 0 266 223" aria-hidden="true">
    <g transform="translate(130 130) scale(0.85)">
      <polygon fill="var(--burst)" points="150,0 119.7,23.8 138.6,57.5 101.4,67.8 106,106 67.8,101.4 57.5,138.6 23.8,119.7 0,150 -23.8,119.7 -57.5,138.6 -67.8,101.4 -106,106 -101.4,67.8 -138.6,57.5 -119.7,23.8 -150,0 -119.7,-23.8 -138.6,-57.5 -101.4,-67.8 -106,-106 -67.8,-101.4 -57.5,-138.6 -23.8,-119.7 0,-150 23.8,-119.7 57.5,-138.6 67.8,-101.4 106,-106 101.4,-67.8 138.6,-57.5 119.7,-23.8"/>
    </g>
  </svg>
  <div class="abs burst-text">
    <div class="cover">** No Cover<br>Charge</div>
    <div class="hours">7 pm - 11 pm</div>
  </div>

  <div class="abs venue">at Velvet Parlor<br>4871 Q Street NE Washington DC 20019</div>

  <div class="abs contact-band">Call Marcus Pelletier at (240) 555-0184 with questions.</div>
</main>
</body>
</html>
```